Pharmacist turned chef in Key West Fl needs a logo design

I am looking for a professional looking business card that says who I am and what I do. For example Chef Dale Morvik, natural organic and health supportive cooking. Phone 555-416-8870 email dalemorvik@quillpost.example web www.thesaltedharvest.example, Key West fl. The color or colors should have some green and other colors that look good together that stimulate appetite and give a clean healthy image. To help with a thought process, words like food as medicine, medicine is food, good nutrition is health but at the same time I do not want a lot of medical symbols that me it look clinical. Any questions please contact me.

```html
<!DOCTYPE html>
<html lang="en">
<head>
<meta charset="utf-8">
<title>Chef Dale Morvik – Business Card</title>
<link rel="stylesheet" href="https://fonts.googleapis.com/css2?family=Arimo:wght@400;700&display=swap">
<style>
  :root {
    --page-bg: #eef1ec;
    --card-green: #9bbd2f;
    --ink-white: #ffffff;
    --ornament-white: #f4f8e8;
    --ornament-edge: #cfe09a;
  }
  html, body {
    margin: 0;
    width: 1200px;
    height: 900px;
    overflow: hidden;
    background: var(--page-bg);
  }
  .canvas {
    position: relative;
    width: 1200px;
    height: 900px;
  }
  .business-card {
    position: absolute;
    left: 100px;
    top: 164px;
    width: 1000px;
    height: 572px;
    border-radius: 60px;
    background: var(--card-green);
    overflow: hidden;
    font-family: "Arimo", Arial, sans-serif;
    color: var(--ink-white);
  }
  .fork-column {
    position: absolute;
    left: 0;
    top: 0;
    width: 150px;
    height: 100%;
    background: linear-gradient(90deg, var(--ink-white) 0%, var(--ink-white) 45%, rgba(255,255,255,0.55) 100%);
  }
  .identity {
    position: absolute;
    left: 220px;
    top: 70px;
  }
  .chef-name {
    margin: 0;
    font-size: 74px;
    font-weight: 400;
    line-height: 1;
    letter-spacing: 0.5px;
  }
  .tagline {
    margin: 14px 0 0;
    font-size: 24px;
    font-weight: 700;
    letter-spacing: 0.3px;
  }
  .contact-list {
    position: absolute;
    left: 240px;
    top: 282px;
    margin: 0;
    padding: 0;
    list-style: none;
    font-size: 24px;
    font-weight: 700;
    white-space: nowrap;
  }
  .contact-list li {
    margin-bottom: 36px;
  }
  .rosette {
    position: absolute;
    left: 670px;
    top: 205px;
    width: 300px;
    height: 300px;
  }
</style>
</head>
<body>
  <main class="canvas">
    <section class="business-card">
      <div class="fork-column" role="img" aria-label="Column of white fork silhouettes along the left edge"></div>

      <header class="identity">
        <h1 class="chef-name">Chef Dale Morvik</h1>
        <p class="tagline">natural organic and health supportive cooking</p>
      </header>

      <ul class="contact-list">
        <li class="contact-phone">555-416-8870</li>
        <li class="contact-email">dalemorvik@quillpost.example</li>
        <li class="contact-web">www.thesaltedharvest.example</li>
      </ul>

      <svg class="rosette" viewBox="0 0 300 300" role="img" aria-label="White spirograph rosette ornament">
        <defs>
          <radialGradient id="rosette-fill" cx="50%" cy="50%" r="50%">
            <stop offset="0%" stop-color="#ffffff"/>
            <stop offset="60%" stop-color="#f4f8e8"/>
            <stop offset="100%" stop-color="#cfe09a"/>
          </radialGradient>
        </defs>
        <circle cx="150" cy="150" r="150" fill="url(#rosette-fill)"/>
        <circle cx="150" cy="150" r="9" fill="#9bbd2f"/>
      </svg>
    </section>
  </main>
</body>
</html>
```